Schema Paladin Powerpoint with Commander Ravelle Type Theme

Need powerpoint template with matching colors and different slide options. Logo and colors to be used can be found at schemapaladinhq.com. Want brightly colored slide deck that is readable form the back of a room, but highlights colors. I will be incorporating Trivano into the slides to gamify my presentations.

Target Market(s)

Tech

Industry/Entity Type

IT, specifically database, but crossing over to mental health in IT, important note this is not for a company, this is just for a professional building a brand

Font styles to use
Sans Serif

Colors
0054AA
0677BA
7BADD7
CADEEF
E8F1F8
EB3D1F
EC4F4E
F09395
F8D3D4
FCEDEE

Requirements
Must have
• My Logo in the bottom corner, front page, a thank your page, question page, content page, content page with two columns, content page with graphs, and icons to be used in the primary colors of the logos, About Me Page, Break Slides, Demo break slide
Should not have
• Lighter shades of colors, I want to pop out where colors are used, I want spacing and font size to be readable from the back of a room, most likely black text and white background

```html
<!DOCTYPE html>
<html lang="en">
<head>
<meta charset="utf-8">
<title>Schema Paladin – Presentation Template Overview</title>
<link href="https://fonts.googleapis.com/css2?family=Mulish:wght@300;400;600;700;800&display=swap" rel="stylesheet">
<style>
:root{
  --red:#E8333A;
  --navy:#1B3F8C;
  --blue:#0A5CB8;
  --cyan:#17A9E1;
  --ink:#1E2A4A;
  --body:#3F4450;
  --grey:#8A8A8A;
  --panel:#ECECEC;
  --page:#FFFFFF;
}
*{box-sizing:border-box;margin:0;padding:0}
html,body{width:1143px;height:1200px;overflow:hidden;background:var(--page);font-family:"Mulish",Arial,sans-serif;color:var(--ink)}
.deck{display:grid;grid-template-columns:repeat(4,254px);grid-auto-rows:143px;column-gap:24px;row-gap:26px;padding:22px 0 0 27px}
.slide{position:relative;overflow:hidden;background:#fff;box-shadow:0 2px 6px rgba(0,0,0,.28)}
.slide.red{background:var(--red)}
.slide.navy{background:var(--navy)}
.slide.blue{background:var(--blue)}
.a{position:absolute}
.disc{position:absolute;border-radius:50%;background:#FCF7F6}
.hero{position:absolute;border-radius:46% 46% 40% 40%;background:radial-gradient(circle at 50% 45%,#E23A44 0 22%,#2B4F9C 48%,#1B3F8C 70%)}
.hero.white{background:radial-gradient(circle at 50% 45%,#E23A44 0 20%,#FFFFFF 44%,#F0F2F7 70%)}
.mark{position:absolute;left:8px;bottom:4px;display:flex;align-items:center;gap:2px;font-size:3.6px;font-weight:800;color:var(--red)}
.mark i{display:block;width:4.5px;height:4.5px;border-radius:50%;background:var(--navy)}
.mark.light{color:#fff}
.mark.light i{background:#fff}
.mark.big{font-size:7px;gap:4px}
.mark.big i{width:10px;height:10px}
.url{position:absolute;right:10px;bottom:4px;font-size:2.8px;color:var(--grey)}
.url b{font-weight:400;margin-left:6px}
.t{font-weight:300;color:var(--ink);line-height:1.05}
.t b{font-weight:800}
.p{font-size:2.7px;line-height:1.42;color:var(--body);text-align:justify}
.p.c{text-align:center}
.sub{font-size:3px;color:var(--grey)}
.bullets{font-size:2.7px;line-height:1.42;color:var(--body);list-style:none}
.bullets li{position:relative;padding-left:4px;margin-bottom:1.4px;text-align:justify}
.bullets li::before{content:"";position:absolute;left:0;top:1.1px;width:1.5px;height:1.5px;border-radius:50%;background:var(--red)}
.ck{position:absolute;display:flex;align-items:center;gap:5px;width:108px}
.tk{position:relative;flex:none;width:14px;height:14px;border-radius:50%;background:#8E8E8E;box-shadow:0 1px 2px rgba(0,0,0,.3)}
.tk::after{content:"";position:absolute;left:4.6px;top:3.2px;width:3.2px;height:5.6px;border:solid #fff;border-width:0 1.1px 1.1px 0;transform:rotate(45deg)}
.tk.n{background:var(--navy)}
.tk.r{background:var(--red)}
.ck strong{display:block;font-size:3.1px;font-weight:800;color:var(--ink);margin-bottom:.8px}
.ck span{display:block;font-size:2.7px;line-height:1.38;color:var(--body)}
.rule{position:absolute;width:.6px;background:#C8C8C8}
.col{position:absolute;background:var(--panel);border-top:1.3px solid var(--navy);box-shadow:0 1px 3px rgba(0,0,0,.18);padding:4px 4px;overflow:hidden}
.col.r{border-top-color:var(--red)}
.col.c{border-top-color:var(--cyan)}
.col.g{border-top-color:#8E8E8E}
.col h4{font-size:2.9px;font-weight:800;color:var(--ink);line-height:1.25;margin-bottom:2.5px}
.col ol{font-size:2.5px;line-height:1.42;color:var(--body);padding-left:4px}
.col ol li{margin-bottom:1.6px}
.num{font-weight:700;line-height:1}
.band{position:absolute;display:flex;align-items:center;color:#fff}
.ic{flex:none;display:block}
.ag{display:flex;flex-direction:column;line-height:1.1}
.ag em{font-style:normal;font-size:4px;color:var(--ink)}
.ag small{font-size:2.7px;color:var(--grey)}
</style>
</head>
<body>
<main class="deck">

<!-- 1 Cover -->
<section class="slide red">
  <div class="disc" style="left:148px;top:-24px;width:196px;height:196px"></div>
  <div class="hero" role="img" aria-label="Hero illustration: a caped figure tearing open a shirt to reveal a chest emblem" style="left:18px;top:30px;width:122px;height:86px"></div>
  <div class="a t" style="left:158px;top:42px;font-size:10px;color:var(--navy)">Your title<br>Presentation<br>Title Template<br>goes here</div>
  <div class="a" style="left:178px;top:98px;font-size:4.6px;color:var(--navy);font-weight:700">Morgan Tessaly</div>
  <div class="a" style="left:163px;top:104px;font-size:2.6px;color:var(--navy)">Data Community Lead, 2020 Impact Award winner</div>
  <div class="mark light"><i></i>Schema Paladin</div>
</section>

<!-- 2 Cover alt -->
<section class="slide red">
  <div class="disc" style="left:122px;top:-26px;width:196px;height:196px"></div>
  <div class="hero" role="img" aria-label="Hero illustration: a caped figure tearing open a shirt to reveal a chest emblem" style="left:128px;top:28px;width:122px;height:88px"></div>
  <div class="a t" style="left:20px;top:40px;width:96px;font-size:10px;color:#fff;text-align:center">Your title<br>Presentation<br>Title Template<br>goes here</div>
  <div class="a" style="left:20px;top:96px;width:96px;text-align:center;font-size:4.6px;color:#fff;font-weight:700">Morgan Tessaly</div>
  <div class="a" style="left:14px;top:102px;width:108px;text-align:center;font-size:2.6px;color:#fff">Data Community Lead, 2020 Impact Award winner</div>
  <div class="mark light"><i></i>Schema Paladin</div>
</section>

<!-- 3 Agenda -->
<section class="slide">
  <div class="a t" style="left:22px;top:44px;font-size:13px">Agenda</div>
  <div class="a sub" style="left:22px;top:60px">Table Of Contents</div>
  <div class="a" style="left:120px;top:34px;display:grid;grid-template-columns:17px 1fr;row-gap:2.6px;align-items:center">
    <span class="num" style="color:var(--red);font-size:8px;font-weight:300">01</span><span class="ag"><em>Introduction</em><small>A short line of sample text for this topic</small></span>
    <span class="num" style="color:var(--red);font-size:8px;font-weight:300">02</span><span class="ag"><em>Topic #1</em><small>A short line of sample text for this topic</small></span>
    <span class="num" style="color:var(--red);font-size:8px;font-weight:300">03</span><span class="ag"><em>Topic #2</em><small>A short line of sample text for this topic</small></span>
    <span class="num" style="color:var(--red);font-size:8px;font-weight:300">04</span><span class="ag"><em>Topic #3</em><small>A short line of sample text for this topic</small></span>
    <span class="num" style="color:var(--red);font-size:8px;font-weight:300">05</span><span class="ag"><em>Topic #4</em><small>A short line of sample text for this topic</small></span>
    <span class="num" style="color:var(--red);font-size:8px;font-weight:300">06</span><span class="ag"><em>Topic #5</em><small>A short line of sample text for this topic</small></span>
    <span class="num" style="color:var(--red);font-size:8px;font-weight:300">07</span><span class="ag"><em>Appendix</em><small>A short line of sample text for this topic</small></span>
  </div>
  <div class="mark"><i></i>Schema Paladin</div><div class="url">schemapaladinhq.com<b>3</b></div>
</section>

<!-- 4 About me -->
<section class="slide">
  <div class="a" role="img" aria-label="Portrait photo of the presenter in front of a fireworks backdrop" style="left:17px;top:28px;width:82px;height:85px;background:linear-gradient(135deg,#2B4F9C 0%,#6F5FA8 45%,#E8333A 100%)"></div>
  <div class="a t" style="left:107px;top:26px;font-size:13px">About <b>Me</b></div>
  <div class="a" style="left:107px;top:40px;font-size:6px;font-weight:300">Morgan Tessaly</div>
  <div class="a" style="left:107px;top:47px;font-size:2.6px;color:var(--grey)">Data Community Lead, 2020 Impact Award winner</div>
  <div class="a p" style="left:107px;top:52px;width:136px;font-size:2.5px">Works as a senior database administrator and has spent many years tuning large data platforms for busy teams. Co-leads a regional user group and a virtual user group, speaks at community events and writes about query performance, automation and monitoring.<br>When not doing things in the data community, likes to be somewhere making a difference. Cares deeply about mental health in tech, sharing lived experience and practical habits that help people stay well at work. Has volunteered with local advocacy groups for many years and now mentors new speakers through their first talks, helping them find their voice and build the confidence to step on stage.<br>You may reach me by messaging me online.</div>
  <div class="mark"><i></i>Schema Paladin</div><div class="url">schemapaladinhq.com<b>4</b></div>
</section>

<!-- 5 Title with text -->
<section class="slide">
  <div class="a t" style="left:20px;top:18px;font-size:12px">Your title slide<br><b>will be here</b></div>
  <div class="a sub" style="left:28px;top:46px;font-size:2.7px">Your great Subtitle goes Here</div>
  <div class="rule" style="left:134px;top:18px;height:42px"></div>
  <div class="a p" style="left:140px;top:17px;width:104px">Sample body copy for this slide shows how a short paragraph sits beside the title. Keep lines brief so the text reads well from the back of the room and the key idea comes through clearly. Use plain words, one idea per sentence and a clear close so every listener can follow along and remember the point.</div>
  <div class="hero" role="img" aria-label="Hero illustration: a caped figure revealing a chest emblem" style="left:16px;top:58px;width:94px;height:66px"></div>
  <ul class="a bullets" style="left:140px;top:60px;width:104px">
    <li>Sample bullet text that explains the first idea in a few short words so the audience can follow it easily.</li>
    <li>Second bullet keeps the same tone and length so the list feels even and balanced.</li>
    <li>Third bullet adds a supporting detail or an example taken from real work in the field.</li>
    <li>Fourth bullet closes the list with a simple takeaway that the whole room can use later.</li>
  </ul>
  <div class="mark"><i></i>Schema Paladin</div><div class="url">schemapaladinhq.com<b>5</b></div>
</section>

<!-- 6 Title with text alt -->
<section class="slide">
  <div class="a t" style="left:20px;top:20px;font-size:12px">Your title slide<br><b>will be here</b></div>
  <div class="rule" style="left:130px;top:18px;height:34px"></div>
  <div class="a p" style="left:136px;top:17px;width:108px">Sample body copy for this slide shows how a short paragraph sits beside the title and keeps the focus clear. Write in plain words so the room can read it while you speak.</div>
  <ul class="a bullets" style="left:20px;top:56px;width:112px">
    <li>Sample bullet text that explains the first idea in a few short words so the audience can follow it easily.</li>
    <li>Second bullet keeps the same tone and length so the list feels even and balanced.</li>
    <li>Third bullet adds a supporting detail or an example taken from real work in the field.</li>
    <li>Fourth bullet closes the list with a simple takeaway that the whole room can use later.</li>
  </ul>
  <div class="hero" role="img" aria-label="Hero illustration: a caped figure revealing a chest emblem" style="left:142px;top:56px;width:94px;height:66px"></div>
  <div class="mark"><i></i>Schema Paladin</div><div class="url">schemapaladinhq.com<b>6</b></div>
</section>

<!-- 7 Demo -->
<section class="slide">
  <div class="a t" style="left:17px;top:18px;font-size:15px">Demo slide title</div>
  <div class="hero" role="img" aria-label="Hero illustration: a caped figure revealing a chest emblem" style="left:16px;top:48px;width:100px;height:72px"></div>
  <div class="ck" style="left:138px;top:48px"><span class="tk n"></span><div><strong>Sample point text here</strong><span>Short supporting line for this point in plain words for the room.</span></div></div>
  <div class="ck" style="left:138px;top:73px"><span class="tk r"></span><div><strong>Sample point text here</strong><span>Short supporting line for this point in plain words for the room.</span></div></div>
  <div class="ck" style="left:138px;top:98px"><span class="tk"></span><div><strong>Sample point text here</strong><span>Short supporting line for this point in plain words for the room.</span></div></div>
  <div class="mark"><i></i>Schema Paladin</div><div class="url">schemapaladinhq.com<b>8</b></div>
</section>

<!-- 8 Demo break -->
<section class="slide">
  <div class="mark big" style="left:58px;top:14px;bottom:auto;font-size:9px"><i style="width:14px;height:14px"></i>Schema Paladin</div>
  <div class="a t" style="left:33px;top:55px;font-size:17px">Demo<br>slide<br>title</div>
  <div class="ck" style="left:130px;top:54px"><span class="tk n"></span><div><strong>Sample point text here</strong><span>Short supporting line for this point in plain words for the room.</span></div></div>
  <div class="ck" style="left:130px;top:79px"><span class="tk r"></span><div><strong>Sample point text here</strong><span>Short supporting line for this point in plain words for the room.</span></div></div>
  <div class="ck" style="left:130px;top:104px"><span class="tk"></span><div><strong>Sample point text here</strong><span>Short supporting line for this point in plain words for the room.</span></div></div>
  <div class="mark"><i></i>Schema Paladin</div><div class="url">schemapaladinhq.com<b>9</b></div>
</section>

<!-- 9 Red blank -->
<section class="slide red">
  <div class="mark big light" style="left:14px;top:12px;bottom:auto"><i></i>Schema Paladin</div>
</section>

<!-- 10 Navy blank -->
<section class="slide navy">
  <div class="mark big light" style="left:14px;top:12px;bottom:auto"><i></i>Schema Paladin</div>
</section>

<!-- 11 Section break -->
<section class="slide red">
  <div class="a" style="left:170px;top:30px;width:40px;height:40px;border-radius:50%;background:#fff"></div>
  <div class="a t" style="left:166px;top:76px;font-size:13px;color:#fff;font-weight:300;letter-spacing:.6px">BREAKE<br>SECTION</div>
  <div class="a" style="left:166px;top:107px;font-size:4px;color:#fff;letter-spacing:.5px">BULLETS SLIDES</div>
</section>

<!-- 12 Stats -->
<section class="slide">
  <div class="a t" style="left:18px;top:16px;font-size:12px">Your title<br><b>slide here</b></div>
  <div class="a sub" style="left:18px;top:44px;font-size:2.7px">Great Subtitle Here</div>
  <div class="rule" style="left:82px;top:16px;height:30px"></div>
  <div class="a p" style="left:88px;top:15px;width:156px">Sample body copy for this slide shows how a longer paragraph sits beside the title and carries the main message across the full width of the slide. Keep it short and plain so it reads well at a distance and sets up the three figures shown below for the audience.</div>
  <div class="a p" style="left:18px;top:54px;width:92px">Use this column to explain the numbers on the right. Give each figure a line of context so the audience knows why it matters and how it was measured. Keep the wording plain and the sentences short so people can follow along while you speak to each point in turn. Close with what the trend means for the team and what you plan to do next, so the figures lead straight into a clear action for everyone in the room.</div>
  <div class="band" style="left:120px;top:54px;width:120px;height:21px;background:var(--navy);padding:3px 0 0 17px;display:block"><b style="font-size:4.2px">1500+</b><div style="font-size:2.6px;line-height:1.3">Short caption that explains this figure<br>and where the number comes from.</div></div>
  <div class="band" style="left:120px;top:78px;width:120px;height:21px;background:var(--red);padding:3px 0 0 17px;display:block"><b style="font-size:4.2px">900+</b><div style="font-size:2.6px;line-height:1.3">Short caption that explains this figure<br>and where the number comes from.</div></div>
  <div class="band" style="left:120px;top:102px;width:120px;height:21px;background:var(--cyan);padding:3px 0 0 17px;display:block"><b style="font-size:4.2px">2900+</b><div style="font-size:2.6px;line-height:1.3">Short caption that explains this figure<br>and where the number comes from.</div></div>
  <div class="mark"><i></i>Schema Paladin</div><div class="url">schemapaladinhq.com<b>7</b></div>
</section>

<!-- 13 Three elements -->
<section class="slide">
  <div class="a t" style="left:0;width:254px;top:22px;font-size:12px;text-align:center">Three <b>elements slide</b></div>
  <div class="a" style="left:21px;top:42px;width:208px;height:22px;background:#fff;box-shadow:0 1px 3px rgba(0,0,0,.2)"><div class="a" style="left:0;top:0;width:64px;height:22px;background:var(--red);color:#fff;font-size:3px;padding:9px 6px">Element One</div><div class="a p" style="left:70px;top:2px;width:134px;font-size:2.5px;font-weight:600">Sample text describing the first element in a few short lines of plain copy, with one clear idea and a short example the audience can read.</div></div>
  <div class="a" style="left:21px;top:72px;width:208px;height:22px;background:#fff;box-shadow:0 1px 3px rgba(0,0,0,.2)"><div class="a" style="left:0;top:0;width:64px;height:22px;background:var(--navy);color:#fff;font-size:3px;padding:9px 6px">Element Two</div><div class="a p" style="left:70px;top:2px;width:134px;font-size:2.5px;font-weight:600">Sample text describing the second element in a few short lines of plain copy, with one clear idea and a short example the audience can read.</div></div>
  <div class="a" style="left:21px;top:102px;width:208px;height:22px;background:#fff;box-shadow:0 1px 3px rgba(0,0,0,.2)"><div class="a" style="left:0;top:0;width:64px;height:22px;background:var(--cyan);color:#fff;font-size:3px;padding:9px 6px">Element Three</div><div class="a p" style="left:70px;top:2px;width:134px;font-size:2.5px;font-weight:600">Sample text describing the third element in a few short lines of plain copy, with one clear idea and a short example the audience can read.</div></div>
  <div class="mark"><i></i>Schema Paladin</div><div class="url">schemapaladinhq.com<b>13</b></div>
</section>

<!-- 14 Text and bullets -->
<section class="slide">
  <div class="a t" style="left:20px;top:22px;font-size:12px">Text and<br><b>Bullets Point</b><br>slide</div>
  <div class="a p" style="left:20px;top:66px;width:82px">Sample paragraph that supports the list on the right. It sums up the idea in a few clear lines so the room can follow the thread while each point is shown. Add a short example or a number to make it concrete, then close with the one thing people should remember after the talk.</div>
  <div class="ck" style="left:126px;top:24px"><span class="tk"></span><div><strong>Sample point text here</strong><span>Short supporting line for this point in plain words for the room.</span></div></div>
  <div class="ck" style="left:126px;top:50px"><span class="tk r"></span><div><strong>Sample point text here</strong><span>Short supporting line for this point in plain words for the room.</span></div></div>
  <div class="ck" style="left:126px;top:76px"><span class="tk"></span><div><strong>Sample point text here</strong><span>Short supporting line for this point in plain words for the room.</span></div></div>
  <div class="ck" style="left:126px;top:102px"><span class="tk"></span><div><strong>Sample point text here</strong><span>Short supporting line for this point in plain words for the room.</span></div></div>
  <div class="mark"><i></i>Schema Paladin</div><div class="url">schemapaladinhq.com<b>14</b></div>
</section>

<!-- 15 Text and bullets mirror -->
<section class="slide">
  <div class="ck" style="left:20px;top:24px"><span class="tk"></span><div><strong>Sample point text here</strong><span>Short supporting line for this point in plain words for the room.</span></div></div>
  <div class="ck" style="left:20px;top:50px"><span class="tk n"></span><div><strong>Sample point text here</strong><span>Short supporting line for this point in plain words for the room.</span></div></div>
  <div class="ck" style="left:20px;top:76px"><span class="tk"></span><div><strong>Sample point text here</strong><span>Short supporting line for this point in plain words for the room.</span></div></div>
  <div class="ck" style="left:20px;top:102px"><span class="tk"></span><div><strong>Sample point text here</strong><span>Short supporting line for this point in plain words for the room.</span></div></div>
  <div class="a t" style="left:143px;top:22px;font-size:12px">Text and<br><b>Bullets Point</b><br>slide</div>
  <div class="a p" style="left:143px;top:66px;width:84px">Sample paragraph that supports the list on the left. It sums up the idea in a few clear lines so the room can follow the thread while each point is shown. Add a short example or a number to make it concrete, then close with the one thing people should remember after the talk.</div>
  <div class="mark"><i></i>Schema Paladin</div><div class="url">schemapaladinhq.com<b>15</b></div>
</section>

<!-- 16 Bullets grid -->
<section class="slide">
  <div class="a t" style="left:0;width:254px;top:22px;font-size:12px;text-align:center">Bullets <b>Point slide</b></div>
  <div class="ck" style="left:20px;top:44px"><span class="tk r"></span><div><strong>Sample point text here</strong><span>Short supporting line for this point in plain words for the room.</span></div></div>
  <div class="ck" style="left:20px;top:71px"><span class="tk"></span><div><strong>Sample point text here</strong><span>Short supporting line for this point in plain words for the room.</span></div></div>
  <div class="ck" style="left:20px;top:98px"><span class="tk"></span><div><strong>Sample point text here</strong><span>Short supporting line for this point in plain words for the room.</span></div></div>
  <div class="ck" style="left:136px;top:44px"><span class="tk n"></span><div><strong>Sample point text here</strong><span>Short supporting line for this point in plain words for the room.</span></div></div>
  <div class="ck" style="left:136px;top:71px"><span class="tk"></span><div><strong>Sample point text here</strong><span>Short supporting line for this point in plain words for the room.</span></div></div>
  <div class="ck" style="left:136px;top:98px"><span class="tk"></span><div><strong>Sample point text here</strong><span>Short supporting line for this point in plain words for the room.</span></div></div>
  <div class="mark"><i></i>Schema Paladin</div><div class="url">schemapaladinhq.com<b>16</b></div>
</section>

<!-- 17 Column break -->
<section class="slide blue">
  <div class="a" style="left:30px;top:26px;width:40px;height:40px;border-radius:50%;background:#fff"></div>
  <div class="a t" style="left:30px;top:74px;font-size:13px;color:#fff;letter-spacing:.6px">COLUMN<br>TEXT<br>SLIDES</div>
</section>

<!-- 18 Two column -->
<section class="slide">
  <div class="a t" style="left:0;width:254px;top:22px;font-size:12px;text-align:center">Two column <b>Text Slide</b></div>
  <div class="col r" style="left:17px;top:43px;width:99px;height:80px"><div class="num" style="color:var(--red);font-size:11px;margin-bottom:5px">01</div><h4>Bullet points title slide here</h4><p class="p" style="font-size:2.5px">Sample text for the first column in a short paragraph that sets up the bullets below in plain words.</p><ul class="bullets" style="font-size:2.5px;margin-top:2px"><li>First sample bullet with a short line of text that adds one detail for the room.</li><li>Second sample bullet with a short line of text that adds one more detail.</li></ul></div>
  <div class="col" style="left:132px;top:43px;width:99px;height:80px"><div class="num" style="color:var(--navy);font-size:11px;margin-bottom:5px">02</div><h4>Bullet points title slide here</h4><p class="p" style="font-size:2.5px">Sample text for the second column in a short paragraph that sets up the bullets below in plain words.</p><ul class="bullets" style="font-size:2.5px;margin-top:2px"><li>First sample bullet with a short line of text that adds one detail for the room.</li><li>Second sample bullet with a short line of text that adds one more detail.</li></ul></div>
  <div class="mark"><i></i>Schema Paladin</div><div class="url">schemapaladinhq.com<b>18</b></div>
</section>

<!-- 19 Three column -->
<section class="slide">
  <div class="a t" style="left:19px;top:22px;font-size:12px">Three column <b>Text Slide</b></div>
  <div class="col" style="left:19px;top:43px;width:64px;height:80px"><h4>Bullet points &amp;<br>Title here</h4><ol><li>Sample line of text for this column item, kept short and plain.</li><li>Another short sample line for this column that adds a detail.</li><li>A third sample line that gives a small example.</li><li>A closing sample line for this column.</li></ol></div>
  <div class="col r" style="left:94px;top:43px;width:64px;height:80px"><h4>Bullet points &amp;<br>Title here</h4><ol><li>Sample line of text for this column item, kept short and plain.</li><li>Another short sample line for this column that adds a detail.</li><li>A third sample line that gives a small example.</li><li>A closing sample line for this column.</li></ol></div>
  <div class="col c" style="left:169px;top:43px;width:64px;height:80px"><h4>Bullet points &amp;<br>Title here</h4><ol><li>Sample line of text for this column item, kept short and plain.</li><li>Another short sample line for this column that adds a detail.</li><li>A third sample line that gives a small example.</li><li>A closing sample line for this column.</li></ol></div>
  <div class="mark"><i></i>Schema Paladin</div><div class="url">schemapaladinhq.com<b>19</b></div>
</section>

<!-- 20 Four column -->
<section class="slide">
  <div class="a t" style="left:19px;top:22px;font-size:12px">Four column <b>Text Slide</b></div>
  <div class="col" style="left:23px;top:43px;width:48px;height:80px"><h4>Bullet points &amp;<br>Title here</h4><ol><li>Sample line of text for this item, kept plain.</li><li>Another short sample line with a detail.</li><li>A third line with a small example.</li><li>A closing sample line.</li></ol></div>
  <div class="col g" style="left:77px;top:43px;width:48px;height:80px"><h4>Bullet points &amp;<br>Title here</h4><ol><li>Sample line of text for this item, kept plain.</li><li>Another short sample line with a detail.</li><li>A third line with a small example.</li><li>A closing sample line.</li></ol></div>
  <div class="col g" style="left:131px;top:43px;width:48px;height:80px"><h4>Bullet points &amp;<br>Title here</h4><ol><li>Sample line of text for this item, kept plain.</li><li>Another short sample line with a detail.</li><li>A third line with a small example.</li><li>A closing sample line.</li></ol></div>
  <div class="col g" style="left:185px;top:43px;width:48px;height:80px"><h4>Bullet points &amp;<br>Title here</h4><ol><li>Sample line of text for this item, kept plain.</li><li>Another short sample line with a detail.</li><li>A third line with a small example.</li><li>A closing sample line.</li></ol></div>
  <div class="mark"><i></i>Schema Paladin</div><div class="url">schemapaladinhq.com<b>20</b></div>
</section>

<!-- 21 Five column -->
<section class="slide">
  <div class="a t" style="left:19px;top:22px;font-size:12px">Five column <b>Text Slide</b></div>
  <div class="col" style="left:21px;top:43px;width:38px;height:80px;padding:3px"><h4>Bullet points &amp;<br>Title here</h4><ol><li>Sample line of text here for this item.</li><li>Another short line with a detail.</li><li>A third short sample line.</li><li>A closing line.</li></ol></div>
  <div class="col r" style="left:64px;top:43px;width:38px;height:80px;padding:3px"><h4>Bullet points &amp;<br>Title here</h4><ol><li>Sample line of text here for this item.</li><li>Another short line with a detail.</li><li>A third short sample line.</li><li>A closing line.</li></ol></div>
  <div class="col g" style="left:107px;top:43px;width:38px;height:80px;padding:3px"><h4>Bullet points &amp;<br>Title here</h4><ol><li>Sample line of text here for this item.</li><li>Another short line with a detail.</li><li>A third short sample line.</li><li>A closing line.</li></ol></div>
  <div class="col g" style="left:150px;top:43px;width:38px;height:80px;padding:3px"><h4>Bullet points &amp;<br>Title here</h4><ol><li>Sample line of text here for this item.</li><li>Another short line with a detail.</li><li>A third short sample line.</li><li>A closing line.</li></ol></div>
  <div class="col g" style="left:193px;top:43px;width:38px;height:80px;padding:3px"><h4>Bullet points &amp;<br>Title here</h4><ol><li>Sample line of text here for this item.</li><li>Another short line with a detail.</li><li>A third short sample line.</li><li>A closing line.</li></ol></div>
  <div class="mark"><i></i>Schema Paladin</div><div class="url">schemapaladinhq.com<b>21</b></div>
</section>

<!-- 22 Six column -->
<section class="slide">
  <div class="a t" style="left:19px;top:19px;font-size:12px">Six column <b>Text Slide</b></div>
  <div class="col g" style="left:19px;top:36px;width:65px;height:41px;padding:2px 3px"><h4 style="margin-bottom:1px">Bullet points &amp; Title here</h4><ol><li>Sample line of text for this item, kept plain.</li><li>Another short sample line with a detail.</li><li>A closing sample line.</li></ol></div>
  <div class="col r" style="left:94px;top:36px;width:65px;height:41px;padding:2px 3px"><h4 style="margin-bottom:1px">Bullet points &amp; Title here</h4><ol><li>Sample line of text for this item, kept plain.</li><li>Another short sample line with a detail.</li><li>A closing sample line.</li></ol></div>
  <div class="col g" style="left:169px;top:36px;width:65px;height:41px;padding:2px 3px"><h4 style="margin-bottom:1px">Bullet points &amp; Title here</h4><ol><li>Sample line of text for this item, kept plain.</li><li>Another short sample line with a detail.</li><li>A closing sample line.</li></ol></div>
  <div class="col g" style="left:19px;top:82px;width:65px;height:41px;padding:2px 3px"><h4 style="margin-bottom:1px">Bullet points &amp; Title here</h4><ol><li>Sample line of text for this item, kept plain.</li><li>Another short sample line with a detail.</li><li>A closing sample line.</li></ol></div>
  <div class="col g" style="left:94px;top:82px;width:65px;height:41px;padding:2px 3px"><h4 style="margin-bottom:1px">Bullet points &amp; Title here</h4><ol><li>Sample line of text for this item, kept plain.</li><li>Another short sample line with a detail.</li><li>A closing sample line.</li></ol></div>
  <div class="col" style="left:169px;top:82px;width:65px;height:41px;padding:2px 3px"><h4 style="margin-bottom:1px">Bullet points &amp; Title here</h4><ol><li>Sample line of text for this item, kept plain.</li><li>Another short sample line with a detail.</li><li>A closing sample line.</li></ol></div>
  <div class="mark"><i></i>Schema Paladin</div><div class="url">schemapaladinhq.com<b>22</b></div>
</section>

<!-- 23 Three text points -->
<section class="slide">
  <div class="col" style="left:18px;top:14px;width:94px;height:33px;padding:2px 3px"><h4 style="margin-bottom:1px">Sample point text here</h4><p class="p" style="font-size:2.4px">Short paragraph for the first point, written in plain words so it reads well at a distance. Add one detail or example to make it concrete for the room.</p></div>
  <div class="col r" style="left:18px;top:51px;width:94px;height:33px;padding:2px 3px"><h4 style="margin-bottom:1px">Sample point text here</h4><p class="p" style="font-size:2.4px">Short paragraph for the second point, written in plain words so it reads well at a distance. Add one detail or example to make it concrete for the room.</p></div>
  <div class="col g" style="left:18px;top:88px;width:94px;height:33px;padding:2px 3px"><h4 style="margin-bottom:1px">Sample point text here</h4><p class="p" style="font-size:2.4px">Short paragraph for the third point, written in plain words so it reads well at a distance. Add one detail or example to make it concrete for the room.</p></div>
  <div class="a t" style="left:124px;top:26px;font-size:12px">Three Text<br><b>Point slide</b></div>
  <div class="a p" style="left:124px;top:62px;width:116px">Sample paragraph that ties the three points together. It restates the main idea, adds a small example and closes with a clear next step so the audience leaves with one message they can remember after the session ends. Keep each sentence short, use everyday words and let the three boxes on the left carry the detail while this text gives the big picture for everyone in the room.</div>
  <div class="mark"><i></i>Schema Paladin</div><div class="url">schemapaladinhq.com<b>23</b></div>
</section>

<!-- 24 Title with icon bands -->
<section class="slide">
  <div class="a t" style="left:18px;top:24px;font-size:12px">Your title<br><b>slide will</b><br>be here</div>
  <div class="a p" style="left:18px;top:70px;width:84px">Sample paragraph that introduces the three services on the right in a few clear lines. Each band names one service and gives a short line about what it offers, kept brief so it reads well.</div>
  <div class="band" style="left:106px;top:22px;width:140px;height:28px;background:var(--navy);padding-left:8px;gap:8px">
    <svg class="ic" width="14" height="14" viewBox="0 0 24 24" fill="none" stroke="#fff" stroke-width="1.8"><rect x="3" y="4" width="14" height="10" rx="1"/><path d="M7 18h6M10 14v4"/><rect x="15" y="9" width="6" height="11" rx="1"/></svg>
    <div><div style="font-size:3.2px">Subtitle Here</div><div style="font-size:2.6px">Short sample line that describes this service.</div></div></div>
  <div class="band" style="left:106px;top:54px;width:140px;height:28px;background:var(--red);padding-left:8px;gap:8px">
    <svg class="ic" width="14" height="14" viewBox="0 0 24 24" fill="none" stroke="#fff" stroke-width="1.8"><path d="M7 18a5 5 0 0 1 0-10 6 6 0 0 1 11 2 4 4 0 0 1 0 8"/><path d="M12 11v8M9 16l3 3 3-3"/></svg>
    <div><div style="font-size:3.2px">Subtitle Here</div><div style="font-size:2.6px">Short sample line that describes this service.</div></div></div>
  <div class="band" style="left:106px;top:86px;width:140px;height:28px;background:var(--cyan);padding-left:8px;gap:8px">
    <svg class="ic" width="14" height="14" viewBox="0 0 24 24" fill="none" stroke="#fff" stroke-width="1.8"><ellipse cx="12" cy="5" rx="7" ry="2.5"/><path d="M5 5v14c0 1.4 3.1 2.5 7 2.5s7-1.1 7-2.5V5M5 12c0 1.4 3.1 2.5 7 2.5s7-1.1 7-2.5"/></svg>
    <div><div style="font-size:3.2px">Subtitle Here</div><div style="font-size:2.6px">Short sample line that describes this service.</div></div></div>
  <div class="mark"><i></i>Schema Paladin</div><div class="url">schemapaladinhq.com<b>24</b></div>
</section>

<!-- 25 Numbered points -->
<section class="slide">
  <div class="a t" style="left:0;width:254px;top:18px;font-size:12px;text-align:center">Your Title <b>Slide Here</b></div>
  <div class="a p" style="left:18px;top:38px;width:106px">Sample paragraph that introduces the four numbered points. It gives the background, explains why each point matters and leads the audience toward the key message. Keep sentences short and the wording plain so every line can be read clearly from the far end of a large room, even on a dim screen. Add a small example from real work to make the idea concrete, then point to the numbers on the right and walk through them one at a time. Finish with a single takeaway that people can act on as soon as the session is over.</div>
  <div class="a p c" style="left:134px;top:40px;width:46px"><div class="num" style="color:var(--navy);font-size:12px;text-align:center">01</div><b style="color:var(--ink)">Sample title text</b><br>Short sample line that explains this point.</div>
  <div class="a p c" style="left:186px;top:40px;width:46px"><div class="num" style="color:var(--navy);font-size:12px;text-align:center">02</div><b style="color:var(--ink)">Sample title text</b><br>Short sample line that explains this point.</div>
  <div class="a p c" style="left:134px;top:84px;width:46px"><div class="num" style="color:var(--cyan);font-size:12px;text-align:center">03</div><b style="color:var(--ink)">Sample title text</b><br>Short sample line that explains this point.</div>
  <div class="a p c" style="left:186px;top:84px;width:46px"><div class="num" style="color:var(--red);font-size:12px;text-align:center">04</div><b style="color:var(--ink)">Sample title text</b><br>Short sample line that explains this point.</div>
  <div class="mark"><i></i>Schema Paladin</div><div class="url">schemapaladinhq.com<b>25</b></div>
</section>

<!-- 26 Title with icons -->
<section class="slide">
  <div class="a t" style="left:17px;top:22px;font-size:12px">Your title<br><b>slide will</b><br>be here</div>
  <div class="a sub" style="left:17px;top:64px;font-size:2.7px">Great Subtitle Here</div>
  <div class="rule" style="left:76px;top:22px;height:44px"></div>
  <div class="a p" style="left:82px;top:21px;width:162px">Sample body copy for this slide shows how a longer paragraph sits beside the title. It carries the main message across the width of the slide and gives enough detail to set up the three ideas below. Keep the wording plain so the room can read it while you talk, and use short sentences so each line lands clearly. Close with a simple bridge into the three ideas so the audience knows what comes next.</div>
  <div class="a" style="left:17px;top:82px;display:flex;gap:6px;width:227px">
    <div style="display:flex;gap:4px;flex:1"><svg class="ic" width="12" height="12" viewBox="0 0 24 24" fill="none" stroke="var(--navy)" stroke-width="2"><path d="M2 12s4-7 10-7 10 7 10 7-4 7-10 7S2 12 2 12z"/><circle cx="12" cy="12" r="3"/></svg><div class="p" style="text-align:left"><b style="color:var(--ink)">Sample text for this idea</b><br>Short paragraph with a few plain words about this idea so the audience can follow it easily.</div></div>
    <div style="display:flex;gap:4px;flex:1"><svg class="ic" width="12" height="12" viewBox="0 0 24 24" fill="none" stroke="var(--navy)" stroke-width="2"><path d="M9 18h6M10 22h4M12 2a7 7 0 0 0-4 12.7V17h8v-2.3A7 7 0 0 0 12 2z"/></svg><div class="p" style="text-align:left"><b style="color:var(--ink)">Sample text for this idea</b><br>Short paragraph with a few plain words about this idea so the audience can follow it easily.</div></div>
    <div style="display:flex;gap:4px;flex:1"><svg class="ic" width="12" height="12" viewBox="0 0 24 24" fill="none" stroke="var(--navy)" stroke-width="2"><rect x="3" y="3" width="18" height="18" rx="1"/><path d="M7 9h4M9 7v4M14 8h4M14 15l3 3M17 15l-3 3M7 16h4"/></svg><div class="p" style="text-align:left"><b style="color:var(--ink)">Sample text for this idea</b><br>Short paragraph with a few plain words about this idea so the audience can follow it easily.</div></div>
  </div>
  <div class="mark"><i></i>Schema Paladin</div><div class="url">schemapaladinhq.com<b>26</b></div>
</section>

<!-- 27 Q&A -->
<section class="slide">
  <svg class="a" style="left:0;top:0" width="254" height="143" viewBox="0 0 254 143" aria-hidden="true">
    <polygon points="118,0 254,0 254,143 90,143 100,120 118,112" fill="var(--navy)"/>
    <polygon points="0,111 201,111 196,118 0,118" fill="var(--red)"/>
  </svg>
  <div class="hero" role="img" aria-label="Emblem illustration of a caped hero" style="left:22px;top:14px;width:64px;height:48px"></div>
  <div class="a" style="left:24px;top:62px;font-size:34px;font-weight:800;color:var(--navy);letter-spacing:-1px;line-height:1">Q&amp;A</div>
  <div class="url" style="color:#C9D3E8">schemapaladinhq.com<b>27</b></div>
</section>

<!-- 28 Thanks -->
<section class="slide red">
  <svg class="a" style="left:0;top:0" width="254" height="143" viewBox="0 0 254 143" aria-hidden="true">
    <path d="M0 24 H104 C124 24 130 60 118 84 C110 100 110 118 96 143 H0 Z" fill="var(--navy)"/>
  </svg>
  <div class="a t" style="left:15px;top:40px;font-size:11px;color:#fff">Contact<br>Information</div>
  <div class="a" style="left:16px;top:84px;font-size:3px;color:#fff;line-height:4.2">
    <div style="display:flex;align-items:center;gap:3px"><span style="width:4px;height:4px;border-radius:50%;background:#fff"></span>@youraccount</div>
    <div style="display:flex;align-items:center;gap:3px"><svg width="5" height="4" viewBox="0 0 10 8" fill="none" stroke="#fff" stroke-width="1"><rect x=".5" y=".5" width="9" height="7"/><path d="M.5 .5l4.5 4 4.5-4"/></svg>you@youraccount.com</div>
    <div style="display:flex;align-items:center;gap:3px"><svg width="5" height="4" viewBox="0 0 10 8" fill="none" stroke="#fff" stroke-width="1"><rect x="1" y=".5" width="8" height="5"/><path d="M0 7.5h10"/></svg>schemapaladinhq.com</div>
  </div>
  <div class="a" style="left:148px;top:58px;font-size:15px;font-weight:800;color:#fff">Thanks</div>
  <div class="a" style="left:157px;top:76px;font-size:4px;color:#fff">For Your watching</div>
  <div class="mark light"><i></i>Schema Paladin</div>
</section>

</main>
</body>
</html>
```